'Cradle Ahead' promotional brochure

We have designed a 6 week program to educate impending first-time parents about the things they need to know to survive the first 6 months. Sessions delivered by general practitioner/family doctor, dietician, physiotherapist, speech pathologist and psychologist. Our promotional blurb is: 'A comprehensive education program for first-time parents-to-be, delivered over 6 weeks by health professionals in your community, about everything you need to know to look after your baby (and yourself!) in the first 6 months'. I now want to put together a promotional brochure to be distributed to those couples who express an interest which will provide further details of what will be delivered in the course.
Updates
In terms of layout, I envisaged a double sided A4 size, foldable into 3 sections, but very happy to be guided on this.
Target Market(s)
To appeal to a young, well educated demographic. First time parents couples.
Industry/Entity Type
Medical
Font styles to use
Other font styles liked:
- Playfair Display
Requirements
Must have
- Playfair display font to be consistent with our logo (attached). Logo also included please. Some consistency with colours of logo please.
Nice to have
- I am a doctor, and have no creative genes! But prefer a clean and professional appearance overall. Not too cluttered in overall appearance.
Should not have
- No cheesy pictures of babies.

```html
<!DOCTYPE html>
<html lang="en">
<head>
<meta charset="utf-8">
<title>Cradle Ahead – Six week course program</title>
<link rel="stylesheet" href="https://fonts.googleapis.com/css2?family=Playfair+Display:wght@400;700;900&family=PT+Serif:ital,wght@0,400;0,700&display=swap">
<style>
  :root {
    --green: #8cc43c;
    --green-soft: #d5e8b6;
    --ink: #1b1b1b;
    --grey-text: #6d6d6d;
    --panel: #e6e6e6;
    --paper: #ffffff;
    --backdrop: #d9d9d9;
    --photo-dark: #3a3a3a;
    --photo-light: #9a9a9a;
  }
  * { box-sizing: border-box; margin: 0; padding: 0; }
  html, body { width: 846px; height: 1200px; overflow: hidden; }
  body { background: var(--backdrop); font-family: "PT Serif", Georgia, serif; color: var(--ink); position: relative; }
  .page { position: absolute; background: var(--paper); overflow: hidden; }
  .page svg.shapes { position: absolute; inset: 0; }
  .block { position: absolute; font-size: 8.6px; line-height: 1.28; }
  .session { color: var(--green); font-weight: 700; font-size: 8.6px; display: block; margin-top: 6px; }
  .session:first-child { margin-top: 0; }
  .block b { font-weight: 700; }
  .block ul { list-style: none; margin-top: 1px; }
  .block li { padding-left: 9px; position: relative; }
  .block li::before { content: ""; position: absolute; left: 1px; top: 4px; width: 3px; height: 3px; background: var(--green); border-radius: 50%; }

  /* Cover */
  .cover { left: 38px; top: 36px; width: 380px; height: 540px; }
  .brand { position: absolute; left: 80px; top: 40px; display: flex; align-items: center; gap: 10px; }
  .brand-dot { width: 34px; height: 34px; border-radius: 50%; background: var(--green); }
  .brand-name { font-family: "Playfair Display", Georgia, serif; font-weight: 400; font-size: 16px; line-height: 1.05; color: var(--ink); letter-spacing: .3px; }
  .cover-title { position: absolute; left: 92px; top: 112px; font-family: "Playfair Display", Georgia, serif; font-weight: 900; font-size: 39px; line-height: 1.05; letter-spacing: .5px; }
  .tagline { position: absolute; left: 200px; top: 282px; width: 170px; font-size: 10px; line-height: 1.2; color: var(--grey-text); }
  .cover-foot { position: absolute; left: 108px; top: 470px; font-family: "Playfair Display", Georgia, serif; font-weight: 700; font-size: 17px; }

  /* Weeks 5–6 page */
  .back { left: 428px; top: 36px; width: 380px; height: 540px; }
  .contact { position: absolute; left: 10px; top: 262px; font-size: 9.4px; line-height: 1.25; color: var(--grey-text); }

  /* Spread weeks 1–4 */
  .spread { left: 38px; top: 612px; width: 770px; height: 560px; }
  .spread-word { position: absolute; font-family: "Playfair Display", Georgia, serif; font-weight: 900; font-size: 34px; color: var(--green); letter-spacing: .5px; }
</style>
</head>
<body>

<section class="page cover">
  <svg class="shapes" width="380" height="540" viewBox="0 0 380 540">
    <defs>
      <linearGradient id="handsTone" x1="0" y1="0" x2="1" y2="1">
        <stop offset="0" stop-color="var(--photo-dark)"/>
        <stop offset="1" stop-color="var(--photo-light)"/>
      </linearGradient>
    </defs>
    <rect x="0" y="110" width="70" height="380" fill="url(#handsTone)" role="img" aria-label="Black and white photo of a parent's hands holding a newborn's feet"/>
    <path d="M50 104 a15 15 0 0 1 30 0 V225 H228 a15 15 0 0 1 0 30 H50 Z" fill="var(--green)"/>
    <rect x="120" y="272" width="120" height="30" rx="15" fill="var(--green)"/>
    <path d="M50 322 H228 a15 15 0 0 1 0 30 H80 V455 a15 15 0 0 1 -30 0 Z" fill="var(--green)"/>
    <rect x="0" y="130" width="10" height="60" rx="5" fill="var(--green)"/>
    <rect x="0" y="372" width="10" height="60" rx="5" fill="var(--green)"/>
    <circle cx="120" cy="400" r="26" fill="var(--green-soft)"/>
  </svg>
  <div class="brand">
    <span class="brand-dot"></span>
    <span class="brand-name">WATTLEBY<br>FAMILY HEALTH</span>
  </div>
  <h1 class="cover-title">CRADLE<br>AHEAD</h1>
  <p class="tagline">A comprehensive education program for first-time parents.</p>
  <p class="cover-foot">Six week course program</p>
</section>

<section class="page back">
  <svg class="shapes" width="380" height="540" viewBox="0 0 380 540">
    <defs>
      <linearGradient id="feetTone" x1="0" y1="0" x2="1" y2="1">
        <stop offset="0" stop-color="var(--photo-light)"/>
        <stop offset="1" stop-color="var(--photo-dark)"/>
      </linearGradient>
    </defs>
    <rect x="10" y="22" width="360" height="228" fill="var(--panel)"/>
    <rect x="10" y="296" width="360" height="226" fill="var(--panel)"/>
    <rect x="300" y="100" width="80" height="340" fill="url(#feetTone)" role="img" aria-label="Black and white photo of a newborn's feet held in parent's hands"/>
    <path d="M330 104 a15 15 0 0 1 30 0 V245 H212 a15 15 0 0 1 0 -30 H330 Z" fill="var(--green)"/>
    <rect x="190" y="262" width="80" height="28" rx="14" fill="var(--green)"/>
    <path d="M212 306 H360 V446 a15 15 0 0 1 -30 0 V336 H212 a15 15 0 0 1 0 -30 Z" fill="var(--green)"/>
    <rect x="370" y="80" width="10" height="60" rx="5" fill="var(--green)"/>
    <rect x="370" y="400" width="10" height="60" rx="5" fill="var(--green)"/>
    <circle cx="300" cy="170" r="26" fill="var(--green-soft)"/>
    <circle cx="300" cy="382" r="24" fill="var(--green-soft)"/>
    <text x="345" y="150" transform="rotate(90 345 150)" text-anchor="middle" dominant-baseline="central" font-family="Playfair Display, Georgia, serif" font-weight="900" font-size="17" fill="var(--ink)">WEEK 5</text>
    <text x="345" y="390" transform="rotate(90 345 390)" text-anchor="middle" dominant-baseline="central" font-family="Playfair Display, Georgia, serif" font-weight="900" font-size="17" fill="var(--ink)">WEEK 6</text>
  </svg>
  <div class="block" style="left:14px; top:30px; width:230px;">
    <span class="session">Session 1</span>
    <b>Clinical Psychologist Dr Mara Lindqvist</b> will share information about bonding and attachment with your baby, how to promote their social and emotional development and how to manage separation anxiety. She will also discuss positive parenting approaches.
  </div>
  <p class="contact">Contact details:<br>T (02) 5550 1234</p>
  <div class="block" style="left:18px; top:352px; width:240px;">
    <span class="session">Session 1</span>
    <b>Secret Men's Business</b> – a men-only session (including beer!) with a new father for frank discussion about the road ahead. Mums will do a shopping excursion with the GP and Dietician to FreshMart to look at baby products and food – the good and the bad!
    <span class="session">Session 2</span>
    <b>Program review, reflection and evaluation</b> and future session planning when baby is six months of age.
  </div>
</section>

<section class="page spread">
  <svg class="shapes" width="770" height="560" viewBox="0 0 770 560">
    <defs>
      <linearGradient id="familyTone" x1="0" y1="0" x2="1" y2="1">
        <stop offset="0" stop-color="var(--photo-light)"/>
        <stop offset="1" stop-color="var(--photo-dark)"/>
      </linearGradient>
    </defs>
    <rect x="20" y="22" width="340" height="214" fill="var(--panel)"/>
    <rect x="410" y="22" width="340" height="196" fill="var(--panel)"/>
    <rect x="20" y="326" width="340" height="214" fill="var(--panel)"/>
    <rect x="410" y="306" width="340" height="234" fill="var(--panel)"/>

    <path d="M300 84 a15 15 0 0 1 30 0 V246 H198 a15 15 0 0 1 0 -30 H300 Z" fill="var(--green)"/>
    <path d="M400 84 a15 15 0 0 1 30 0 V216 H548 a15 15 0 0 1 0 30 H400 Z" fill="var(--green)"/>
    <path d="M198 318 H330 V466 a15 15 0 0 1 -30 0 V348 H198 a15 15 0 0 1 0 -30 Z" fill="var(--green)"/>
    <path d="M400 308 H548 a15 15 0 0 1 0 30 H430 V466 a15 15 0 0 1 -30 0 Z" fill="var(--green)"/>
    <rect x="352" y="72" width="24" height="80" rx="12" fill="var(--green)"/>
    <rect x="372" y="412" width="24" height="80" rx="12" fill="var(--green)"/>
    <rect x="190" y="266" width="96" height="30" rx="15" fill="var(--green)"/>
    <rect x="484" y="266" width="96" height="30" rx="15" fill="var(--green)"/>

    <circle cx="385" cy="282" r="62" fill="url(#familyTone)" role="img" aria-label="Black and white photo of a young couple holding their baby"/>
    <circle cx="262" cy="166" r="26" fill="var(--green-soft)"/>
    <circle cx="270" cy="400" r="26" fill="var(--green-soft)"/>
    <circle cx="470" cy="370" r="22" fill="var(--green-soft)"/>

    <g font-family="Playfair Display, Georgia, serif" font-weight="900" font-size="17" fill="var(--ink)">
      <text x="315" y="148" transform="rotate(90 315 148)" text-anchor="middle" dominant-baseline="central">WEEK 1</text>
      <text x="415" y="148" transform="rotate(90 415 148)" text-anchor="middle" dominant-baseline="central">WEEK 3</text>
      <text x="315" y="400" transform="rotate(90 315 400)" text-anchor="middle" dominant-baseline="central">WEEK 2</text>
      <text x="415" y="400" transform="rotate(90 415 400)" text-anchor="middle" dominant-baseline="central">WEEK 4</text>
    </g>
  </svg>

  <span class="spread-word" style="left:32px; top:258px;">CRADLE</span>
  <span class="spread-word" style="left:598px; top:258px;">AHEAD</span>

  <div class="block" style="left:28px; top:34px; width:256px;">
    <b>GP Dr Fiona Hartley</b> will share information for Mum's own health after delivery. Topics include:
    <ul>
      <li>Vaccinations in pregnancy</li>
      <li>Bleeding, bladder and bowel after delivery</li>
      <li>Breastfeeding, engorgement and mastitis</li>
      <li>Bottle feeding</li>
      <li>Post-natal anxiety &amp; depression</li>
      <li>Intimacy and contraception</li>
    </ul>
  </div>

  <div class="block" style="left:446px; top:30px; width:296px;">
    <span class="session">Session 1</span>
    <b>Dietician Anna Brennan</b> provides advice for Mums regarding healthy eating during pregnancy and lactation, normal weight gain during pregnancy and realistic weight loss after. She will also discuss the evidence regarding breastfeeding VS bottle-feeding, normal infant weight gain and introducing solids (including those with potential for allergy).
    <span class="session">Session 2</span>
    <b>Paediatric Speech Pathologist Ruth Calloway</b> will share information about latching and breast-feeding troubles and tongue tie, advice about dummies and finger-sucking, introducing solids and feeding (including 'pouch' food), encouraging language development and current evidence about electronic devices impacting language development.
  </div>

  <div class="block" style="left:28px; top:350px; width:262px;">
    <span class="session">Session 1</span>
    <b>Clinical Psychologist Dr Mara Lindqvist</b> will discuss changes in relationships as couples become parents, gender roles in parenting and post-natal depression.
    <span class="session">Session 2</span>
    <b>Physiotherapist Tessa Moreland</b> will present advice for Mums regarding exercise during and after pregnancy, looking after the pelvic floor during and after pregnancy, and abdominal muscle separation management. She will also provide advice for promoting babies' neck strength and minimising the risk of flat spots on the head and encouraging gross motor skills in the first six months
  </div>

  <div class="block" style="left:446px; top:352px; width:296px;">
    <b>GP Dr Fiona Hartley</b> will share advice about your babies' health in the first six months, including:
    <ul>
      <li>Skin of newborns</li>
      <li>Sleeping</li>
      <li>Crying</li>
      <li>Immunisations</li>
      <li>Fever and infections</li>
      <li>Diarrhoea and constipation</li>
      <li>Teething</li>
      <li>Understanding a baby's signals</li>
    </ul>
  </div>
</section>

</body>
</html>
```